Family Entertainment Center needs a fundraising flyer design

We need a 8.5 x 5.5 (half sheet of copy paper) flyer designed for a roller skating rink/family entertainment center in Wichita, KS. We partner with 100s of local schools each year by offering PTO fundraisers at our facility. With each party we send out flyers to the schools to send home with each kid to remind them of the time and date of the party as well as get them excited! Most of these schools and PTOs call these fundraisers "skate night".The information we need communicated or on our flyer is below:-Skating $6-Play Zone $6-Skate & Play $10-Skate Rental is included in above pricing-Price is per person-www.maplewheelrink.com-Maplewood Skate Center 847 S. Pinecrest Ave. Wichita, KS 67219-Our logo (attached)-The words or heading "Skate Night"-A blank, white space for us to print details in (see attached flyer for an example)

Target Market(s)

Elementary School parents and kids

Font styles to use
Serif
Sans Serif

Requirements
Must have
• The information outlined in the description and a blank white space incorporated into the design for our ability to print over.
Nice to have
• colors that match or compliment our logo, creative, but clean fonts

```html
<!DOCTYPE html>
<html lang="en">
<head>
<meta charset="utf-8">
<title>Skate Night Flyer</title>
<link href="https://fonts.googleapis.com/css2?family=Teko:wght@500;600&display=swap" rel="stylesheet">
<style>
  :root{
    --sky-deep:#0a4fa8;
    --sky-mid:#1c86d8;
    --sky-light:#8fd0f4;
    --banner:#1d4f9a;
    --banner-dark:#14386f;
    --stitch:#9cc4ee;
    --orange:#f9a51b;
    --white:#ffffff;
    --black:#0b0b0b;
    --cloud-edge:#8a8f96;
    --badge:#1b3f7c;
    --badge-ring:#e8ecf1;
    --dark-disc:#0d1620;
  }
  *{margin:0;padding:0;box-sizing:border-box}
  html,body{width:1200px;height:816px;overflow:hidden;background:#fff}
  .flyer{
    position:relative;width:1200px;height:816px;overflow:hidden;
    background:
      radial-gradient(ellipse 420px 260px at 150px 420px, rgba(255,255,255,.55), transparent 70%),
      radial-gradient(ellipse 300px 160px at 560px 90px, rgba(255,255,255,.35), transparent 70%),
      linear-gradient(160deg, var(--sky-light) 0%, var(--sky-mid) 40%, var(--sky-deep) 100%);
    font-family:'Teko', 'Arial Narrow', sans-serif;
  }
  .photo{
    position:absolute;border:6px solid var(--white);
    box-shadow:0 6px 16px rgba(0,0,0,.35);
  }
  .photo--climber{left:-20px;top:-20px;width:260px;height:210px;transform:rotate(-4deg);
    background:linear-gradient(135deg,#1e2a6a,#3b63b8 55%,#6d2a2a)}
  .photo--group-skaters{left:612px;top:6px;width:280px;height:196px;transform:rotate(5deg);
    background:linear-gradient(160deg,#4b3c9a,#b8c6e4 70%,#d8dcee)}
  .photo--rink{left:878px;top:18px;width:340px;height:400px;transform:rotate(-4deg);
    background:linear-gradient(170deg,#3a2f7a,#7f9be0 45%,#cdd6f2)}
  .photo--class{left:697px;top:186px;width:282px;height:226px;transform:rotate(-2deg);
    background:linear-gradient(170deg,#c7a98f,#b24a3c 55%,#2f3b6b)}
  .photo--arcade{left:185px;top:488px;width:296px;height:250px;transform:rotate(-5deg);
    background:linear-gradient(150deg,#6a2a2a,#c9a36b 45%,#8fb5cf)}
  .cloud{position:absolute;left:30px;top:40px;width:700px;height:470px}
  .dark-disc{position:absolute;left:-60px;top:560px;width:330px;height:330px;border-radius:50%;background:var(--dark-disc)}
  .thought-dots{position:absolute;left:40px;top:500px}
  .brand{
    position:absolute;left:64px;top:600px;width:190px;height:190px;border-radius:50%;
    background:var(--badge);border:7px solid var(--badge-ring);
    display:flex;align-items:center;justify-content:center;text-align:center;
    color:var(--white);font-weight:600;font-size:31px;line-height:.95;letter-spacing:1px;
    text-transform:uppercase;padding-top:8px;
  }
  .title-banner{
    position:absolute;left:516px;top:418px;width:586px;height:134px;
    background:linear-gradient(180deg,var(--banner),var(--banner-dark));
    border-radius:6px;box-shadow:0 6px 14px rgba(0,0,0,.4);
  }
  .title-banner::before{
    content:"";position:absolute;inset:7px;border:2px dashed var(--stitch);border-radius:4px;
  }
  .title-banner h1{
    position:absolute;inset:0;display:flex;align-items:center;justify-content:center;
    color:var(--white);font-weight:600;font-size:108px;letter-spacing:3px;
    text-transform:uppercase;padding-top:14px;text-shadow:0 3px 6px rgba(0,0,0,.35);
    transform:scaleX(.8);white-space:nowrap;
  }
  .pricing{
    position:absolute;left:418px;top:566px;width:800px;text-align:center;
    color:var(--orange);font-weight:600;font-size:52px;text-transform:uppercase;
    letter-spacing:.5px;text-shadow:0 2px 4px rgba(0,0,0,.4);white-space:nowrap;
    transform:scaleX(.76);transform-origin:center;
  }
  .rental{
    position:absolute;left:510px;top:636px;width:600px;text-align:center;
    color:var(--white);font-weight:500;font-size:35px;text-transform:uppercase;
    text-shadow:0 2px 4px rgba(0,0,0,.4);white-space:nowrap;
  }
  .info-bar{
    position:absolute;left:517px;width:592px;height:27px;background:var(--black);
    color:var(--white);font-weight:500;font-size:22px;letter-spacing:1.2px;
    text-transform:uppercase;text-align:center;line-height:31px;white-space:nowrap;
    overflow:hidden;
  }
  .info-bar--web{top:687px}
  .info-bar--address{top:720px}
  .info-bar .venue{color:var(--orange)}
</style>
</head>
<body>
<main class="flyer">
  <div class="photo photo--climber" role="img" aria-label="Photo of a smiling boy climbing in the play zone"></div>
  <div class="photo photo--rink" role="img" aria-label="Photo of a girl roller skating on the rink with the play structure behind"></div>
  <div class="photo photo--group-skaters" role="img" aria-label="Photo of four girls posing on roller skates"></div>
  <div class="photo photo--class" role="img" aria-label="Photo of a group of cheering school kids"></div>

  <svg class="cloud" viewBox="0 0 700 470" aria-label="Blank space for event details">
    <g fill="var(--cloud-edge)">
      <circle cx="150" cy="150" r="118"/><circle cx="300" cy="110" r="112"/>
      <circle cx="450" cy="115" r="105"/><circle cx="570" cy="185" r="100"/>
      <circle cx="560" cy="320" r="100"/><circle cx="420" cy="360" r="100"/>
      <circle cx="270" cy="360" r="104"/><circle cx="130" cy="300" r="108"/>
      <rect x="120" y="140" width="460" height="220"/>
    </g>
    <g fill="var(--white)">
      <circle cx="150" cy="150" r="106"/><circle cx="300" cy="110" r="100"/>
      <circle cx="450" cy="115" r="93"/><circle cx="570" cy="185" r="88"/>
      <circle cx="560" cy="320" r="88"/><circle cx="420" cy="360" r="88"/>
      <circle cx="270" cy="360" r="92"/><circle cx="130" cy="300" r="96"/>
      <rect x="120" y="140" width="460" height="220"/>
    </g>
  </svg>

  <div class="photo photo--arcade" role="img" aria-label="Photo of three girls playing an arcade game"></div>

  <div class="dark-disc"></div>
  <svg class="thought-dots" width="160" height="120" aria-hidden="true">
    <ellipse cx="110" cy="38" rx="34" ry="26" fill="var(--cloud-edge)"/>
    <ellipse cx="110" cy="38" rx="27" ry="20" fill="var(--white)"/>
    <ellipse cx="48" cy="98" rx="26" ry="20" fill="var(--cloud-edge)"/>
    <ellipse cx="48" cy="98" rx="20" ry="14" fill="var(--white)"/>
  </svg>
  <div class="brand">Maplewood<br>Skate</div>

  <div class="title-banner"><h1>Skate Night</h1></div>
  <p class="pricing">Skating $6-Play Zone $6-Skate &amp; Play $10</p>
  <p class="rental">Skate Rental is included in above pricing</p>
  <p class="info-bar info-bar--web">Price is per person-www.maplewheelrink.com</p>
  <p class="info-bar info-bar--address"><span class="venue">Maplewood Skate Center</span> 847 S. Pinecrest Ave. Wichita, KS 67219</p>
</main>
</body>
</html>
```